Flu Brochure- brief and easy-to-read

A team of health educators is looking to design a brochure on what Americans need to "know and do" when it comes to flu season. All copy and images will be provided.

The brochure needs to be an 8.5 x 11 inch bi-fold design.

I am only able to upload up to 5 files. So, additional images will have to sent via dropbox or some other mechanism.

Target Market(s)

The audience is vast, but the content and design need to be simple and engaging.

Industry/Entity Type

Health

Requirements
Must have
• Must Have:
- Clear and Simple, Easy-to-read and Understand and Act on- should be very focused on what the consumer should do about taking care of themselves when it comes to the flu.

We will provide all of the copy for the brochure design. We will also provide photographs for the project.

Captions for photographs that support the key message.

Should Not Have:
- x reverse print- e.g., no white font on a black background
x fancy fonts or heavy use of italics
x use of all capitals
x no full justification
x no use of drop caps

Must be multicultural as well.

```html
<!DOCTYPE html>
<html lang="en">
<head>
<meta charset="utf-8">
<title>Flu Brochure Spread</title>
<link href="https://fonts.googleapis.com/css2?family=Archivo+Black&family=Arimo:wght@400;700&display=swap" rel="stylesheet">
<style>
  :root {
    --bg: #e9e6e1;
    --page-blue: #1fa6e6;
    --tab-blue: #c8ecfc;
    --ink-blue: #1c5ea9;
    --title-blue: #0b58a6;
    --orange: #f2561d;
    --red: #e3262d;
    --white: #ffffff;
    --footer-ink: #1b5aa0;
  }
  * { box-sizing: border-box; margin: 0; padding: 0; }
  html, body { width: 1200px; height: 1000px; overflow: hidden; }
  body {
    background: var(--bg);
    font-family: "Arimo", Arial, sans-serif;
    position: relative;
  }
  .spread {
    position: absolute; left: 50px; top: 100px;
    width: 1100px; height: 800px;
    display: flex;
    box-shadow: 0 10px 30px rgba(0,0,0,.18);
  }
  .page { position: relative; width: 550px; height: 800px; overflow: hidden; }

  /* Left page */
  .page-treat { background: var(--page-blue); }
  .section-tab {
    position: absolute; left: 20px; top: 40px; width: 250px; height: 38px;
    background: var(--tab-blue); color: var(--ink-blue);
    border-radius: 0 10px 10px 0;
    font-size: 27px; display: flex; align-items: center; padding-left: 22px; gap: 18px;
    z-index: 2;
  }
  .section-tab .num { font-weight: 700; font-size: 24px; }
  .treat-panel {
    position: absolute; left: 22px; top: 62px; right: 18px; bottom: 22px;
    background: var(--white);
    border-radius: 0 46px 18px 18px;
    padding: 54px 34px 26px 34px;
    color: var(--ink-blue);
    font-size: 16.5px; line-height: 1.25;
    display: flex; flex-direction: column;
  }
  .panel-heading { color: var(--orange); font-size: 18.5px; font-weight: 400; margin: 0 0 16px; }
  .treat-panel p { margin-bottom: 8px; }
  .sub-list { list-style: none; margin: 0 0 22px 18px; }
  .sub-list li::before { content: "- "; }
  .action-list { list-style: none; margin-bottom: 18px; }
  .action-list li { position: relative; padding-left: 22px; margin-bottom: 9px; }
  .action-list li::before {
    content: ""; position: absolute; left: 2px; top: 6px; width: 7px; height: 7px;
    border-right: 2.5px solid var(--ink-blue); border-top: 2.5px solid var(--ink-blue);
    transform: rotate(45deg);
  }
  .action-list li.warning { color: var(--red); }
  .action-list li.warning::before { display: none; }
  .action-list li.warning svg { position: absolute; left: 0; top: 2px; }
  .fever-free { color: var(--orange); font-weight: 700; }
  .info-block { margin-top: auto; font-size: 12.5px; line-height: 1.25; color: var(--ink-blue); }
  .info-block .info-title { color: var(--orange); font-weight: 700; }

  /* Right page */
  .page-cover { background: var(--white); }
  .cover-title {
    position: absolute; left: 0; right: 0; top: 18px; text-align: center;
    font-family: "Archivo Black", "Arial Black", sans-serif;
    font-size: 168px; line-height: 1; color: var(--title-blue); letter-spacing: 4px;
  }
  .cover-question {
    position: absolute; left: 30px; right: 30px; top: 200px; text-align: center;
    color: var(--orange); font-size: 20px; line-height: 1.25;
  }
  .photo-frame {
    position: absolute; left: 24px; right: 14px; top: 264px; height: 400px;
    background: var(--page-blue); border-radius: 0 0 30px 30px; padding: 14px 14px 22px 14px;
  }
  .photo {
    width: 100%; height: 100%; border-radius: 22px;
    background: linear-gradient(135deg, #d8dde0 0%, #b9b4ad 40%, #e4dccf 70%, #f3efe8 100%);
  }
  .topic-list { position: absolute; left: 24px; top: 474px; list-style: none; }
  .topic-list li {
    display: flex; align-items: center; gap: 22px;
    width: 200px; height: 32px; margin-bottom: 8px; padding-left: 14px;
    background: rgba(255,255,255,.82); color: var(--title-blue);
    font-size: 26px; border-radius: 0 6px 6px 0;
  }
  .topic-list .num { font-weight: 700; font-size: 23px; width: 16px; }
  .cover-footer {
    position: absolute; left: 40px; right: 30px; top: 692px;
    color: var(--footer-ink); font-size: 12px; line-height: 1.35;
  }
  .sponsor { margin-top: 12px; font-size: 12.5px; display: flex; align-items: center; gap: 8px; }
  .sponsor-name { color: var(--red); font-size: 15px; }
</style>
</head>
<body>
  <main class="spread">
    <section class="page page-treat">
      <div class="section-tab"><span class="num">4</span><span>Treat</span></div>
      <div class="treat-panel">
        <h2 class="panel-heading">What If Someone Has The Flu?</h2>
        <p>If you think someone in your family has the flu, call your doctor.</p>
        <ul class="sub-list">
          <li>Ask if they need to be seen.</li>
          <li>Ask your doctor about flu medicine.</li>
        </ul>
        <h2 class="panel-heading">If Your Doctor Tells You To Treat Yourself...</h2>
        <ul class="action-list">
          <li>Stay home and rest – don't spread your germs to others!</li>
          <li>Take medicines for fever, such as acetaminophen (Feverease®) or ibuprofen (Remedol®, Achefree®, Calmprin®).</li>
          <li class="warning">
            <svg width="15" height="15" viewBox="0 0 15 15" aria-hidden="true"><circle cx="7.5" cy="7.5" r="6" fill="none" stroke="#e3262d" stroke-width="2"/><line x1="3.5" y1="11.5" x2="11.5" y2="3.5" stroke="#e3262d" stroke-width="2"/></svg>
            Do not take aspirin for fever.</li>
          <li>Drink 6-8 big glasses of water, juice, or sports drink (like Hydrapeak®, Sportlyte®) every day.</li>
          <li>If around other people, wear a mask.</li>
        </ul>
        <h2 class="panel-heading">Once you start feeling better...</h2>
        <p>You still want to make sure you don't get other people sick.</p>
        <p>Stay at home until you are <span class="fever-free">"fever-free"</span> for at least 24 hours without the help of medicine.</p>
        <div class="info-block">
          <div class="info-title">For reliable info on flu:</div>
          <div>Call your doctor</div>
          <div>Go to: http://www.fluready-info.org/</div>
          <div>Call 1-800-555-0142</div>
        </div>
      </div>
    </section>

    <section class="page page-cover">
      <h1 class="cover-title">FLU</h1>
      <p class="cover-question">What are 4 things I can do to prepare for<br>the flu season and keep my family healthy?</p>
      <div class="photo-frame">
        <div class="photo" role="img" aria-label="Photo of a woman wrapped in a blanket on a sofa, blowing her nose and holding a thermometer"></div>
      </div>
      <ol class="topic-list">
        <li><span class="num">1</span>Know</li>
        <li><span class="num">2</span>Prevent</li>
        <li><span class="num">3</span>Protect</li>
        <li><span class="num">4</span>Treat</li>
      </ol>
      <footer class="cover-footer">
        <p>©2013. Harbor Health Literacy Team. Northfield University. Alder L, Brooks KL, Carver RM. Content based on scientific evidence from the National Health Dept. and the National Disease Control Agency (NDCA) as of March 2013.</p>
        <p class="sponsor">Sponsored by: <span class="sponsor-name">Meridian Care</span></p>
      </footer>
    </section>
  </main>
</body>
</html>
```